GLOW AT NOON (EP) FOR KEMASO, AN ARTISTE SIGNED TO LANTERN ENTERTAINMENTS

A CREATIVELY SIMPLE EVERGREEN DESIGN. BECAUSE NO PICTURE IS REQUIRED, THE DESIGN HAS TO BE VERY EYE CATCHING AND COLOURFUL AND I WANT THE BEST CONCEPT TO DESCRIBE THE TITLE.

DETAILS TO BE USED ON THE DESIGN AS FOLLOWS

RECORDING LABEL: LANTERN ENTERTAINMENTS
ARTISTE NAME: KEMASO
EP TITLE: GLOW AT NOON
TRACK LIST
1. EKE DURADE (Produced by Zumol)
2. ROOFTOP PARADE (Produced by K.R.V Beats)
3. U SEF TAYE (PRODUCED BY B'KEYZ)
4. UNDER THE GOLDEN EVENING SUN (PRODUCED BY GRIMBO JAY)
5. RISE GLIDE SHINE (PRODUCED BY VELKU)

ALL SONGS MIXED BY ZEK MORROW.

Target Market(s)

AFRICA

Font styles to use
Serif
Sans Serif
Decorative
Script

Colors

Designer to choose colors to be used in the design.

Requirements
Must have
• A CREATIVELY SIMPLE EVERGREEN DESIGN
Nice to have
Should not have
• NON

```html
<!DOCTYPE html>
<html lang="en">
<head>
<meta charset="utf-8">
<title>KEMASO – GLOW AT NOON</title>
<link rel="stylesheet" href="https://fonts.googleapis.com/css2?family=Audiowide&family=Bowlby+One&family=Roboto+Condensed:ital,wght@0,400;1,400&family=Permanent+Marker&family=Arimo:wght@700&display=block">
<style>
  :root {
    --sun-glow: #fdfde2;
    --lime: #d4ee78;
    --leaf: #86d038;
    --meadow: #46a82a;
    --lake-pink: #f5c8ea;
    --bark: #2e1230;
    --bark-mid: #5a2a4e;
    --leaf-bright: #7fd43a;
    --leaf-orange: #f06a24;
    --leaf-blue: #2f7fe0;
    --artist: #b3107a;
    --title-green: #2f8f1c;
    --title-edge: #f4ec2a;
    --ink: #3b1d4c;
    --black: #111111;
    --mask-dark: #6b2a1c;
    --mask-warm: #c8562a;
  }
  * { margin: 0; padding: 0; box-sizing: border-box; }
  html, body { width: 1200px; height: 1096px; overflow: hidden; background: #ffffff; }
  .cover { position: relative; width: 1200px; height: 1096px; overflow: hidden; }

  .scenery {
    position: absolute; inset: 0;
    background:
      radial-gradient(ellipse 560px 340px at 800px 300px, var(--sun-glow) 0%, rgba(253,253,226,0) 100%),
      linear-gradient(180deg,
        #eef7c0 0%, var(--lime) 34%, #e0f296 56%,
        var(--lake-pink) 63%, #fae6f4 72%,
        var(--leaf) 82%, var(--meadow) 100%);
  }
  .tree-art {
    position: absolute; left: -40px; top: -20px;
    width: 700px; height: 1140px;
    border-radius: 0 60% 40% 0 / 0 50% 50% 0;
    background:
      radial-gradient(circle 170px at 300px 330px, rgba(47,127,224,0.55) 0%, rgba(47,127,224,0) 100%),
      radial-gradient(circle 200px at 120px 560px, rgba(240,106,36,0.6) 0%, rgba(240,106,36,0) 100%),
      radial-gradient(ellipse 300px 240px at 460px 700px, rgba(127,212,58,0.9) 0%, rgba(127,212,58,0) 100%),
      radial-gradient(ellipse 260px 200px at 330px 480px, rgba(127,212,58,0.85) 0%, rgba(127,212,58,0) 100%),
      linear-gradient(90deg, var(--bark) 0%, var(--bark-mid) 22%, rgba(90,42,78,0.35) 48%, rgba(90,42,78,0) 80%);
  }
  .mask-art {
    position: absolute; left: 830px; top: 615px;
    width: 130px; height: 190px;
    border-radius: 48% 48% 50% 50% / 30% 30% 70% 70%;
    background: linear-gradient(180deg, var(--mask-warm) 0%, var(--mask-dark) 100%);
  }

  .headline {
    position: absolute; left: 600px; width: 460px;
    text-align: center;
  }
  .artist {
    top: 66px;
    font-family: "Audiowide", sans-serif;
    font-size: 42px;
    letter-spacing: 3px;
    color: var(--artist);
  }
  .ep-title {
    top: 140px;
    font-family: "Bowlby One", sans-serif;
    font-size: 50px;
    line-height: 1;
    color: var(--title-green);
    -webkit-text-stroke: 3px var(--title-edge);
    paint-order: stroke fill;
    transform: scaleY(1.25);
  }
  .label {
    top: 222px;
    font-family: "Arimo", sans-serif;
    font-weight: 700;
    font-size: 22px;
    color: var(--ink);
  }
  .tracklist {
    position: absolute; left: 493px; top: 278px;
    font-family: "Roboto Condensed", sans-serif;
    color: var(--ink);
  }
  .tracklist h2 {
    font-style: italic;
    font-weight: 400;
    font-size: 23px;
    line-height: 40px;
  }
  .tracklist ol { list-style: none; }
  .tracklist li {
    font-size: 23px;
    line-height: 47px;
    white-space: nowrap;
  }
  .credit {
    position: absolute; left: 743px; top: 556px;
    font-family: "Permanent Marker", cursive;
    font-size: 22px;
    color: var(--black);
    white-space: nowrap;
  }
</style>
</head>
<body>
  <main class="cover">
    <div class="scenery" role="img" aria-label="Bright sunlit meadow with leafy trees, a pink pond and green grass"></div>
    <div class="tree-art" role="img" aria-label="Swirling dark tree with bright green, orange and blue leaves drifting across the scene"></div>
    <div class="mask-art" role="img" aria-label="Colourful African tribal mask illustration"></div>

    <div class="headline artist">KEMASO</div>
    <h1 class="headline ep-title">GLOW AT NOON</h1>
    <div class="headline label">LANTERN ENTERTAINMENTS</div>

    <section class="tracklist">
      <h2>TRACK LIST</h2>
      <ol>
        <li>1. EKE DURADE (Produced by Zumol)</li>
        <li>2. ROOFTOP PARADE (Produced by K.R.V Beats)</li>
        <li>3. U SEF TAYE (PRODUCED BY B'KEYZ)</li>
        <li>4. UNDER THE GOLDEN EVENING SUN (PRODUCED BY GRIMBO JAY)</li>
        <li>5. RISE GLIDE SHINE (PRODUCED BY VELKU)</li>
      </ol>
    </section>

    <p class="credit">ALL SONGS MIXED BY ZEK MORROW.</p>
  </main>
</body>
</html>
```